Business Cards for Law Office of Denise R. Harlow

I need a business card for my new estate planning law firm. I have attached my logo. I would like a design that is professional but not too formal or stuffy.

Target Market(s)

Professionals (lawyers, doctors, businesswomen) between the age of 30 and 50 who are tech-savvy and educated.

Industry/Entity Type

Lawyer

Contact Information for Business Card

Denise R. Harlow

528 E. 19th Street
7th Floor
New York, NY 10583

Phone: (855) 602-7318
Direct: (917) 463-5071
Email: Denise@DeniseRHarlowLegal.test
www.DeniseRHarlowLegal.test

Font styles to use
Other font styles liked:
• Corbel

Requirements
Must have
• On the front:
• Denise R. Harlow, Esq.
• Owner & Founder
• 528 E. 19th Street
• 7th Floor
• New York, NY 10583
• Phone: (855) 602-7318
• Direct: (917) 463-5071
• Email: denise@deniserharlowlegal.test
• www.deniserharlowlegal.test
• On the back:
• LOGO
Nice to have
• I want it to be professional but not too formal or stuffy. Please choose colors that go with my logo.
Should not have
• I don't want TOO MUCH color. Some color is good, but not too much.

```html
<!DOCTYPE html>
<html lang="en">
<head>
<meta charset="utf-8">
<title>Business Cards – Law Office of Denise R. Harlow</title>
<link href="https://fonts.googleapis.com/css2?family=Source+Sans+3:wght@400;600&display=swap" rel="stylesheet">
<style>
  :root {
    --stage-top: #262626;
    --stage-bottom: #040404;
    --card-white: #ffffff;
    --brand-purple: #7a297c;
    --ink: #1d1d1d;
    --card-radius: 10px;
  }
  html, body {
    margin: 0;
    padding: 0;
    width: 1200px;
    height: 900px;
    overflow: hidden;
  }
  body {
    position: relative;
    background: linear-gradient(180deg, var(--stage-top) 0%, #141414 55%, var(--stage-bottom) 100%);
    font-family: "Source Sans 3", "Segoe UI", sans-serif;
  }
  .card {
    position: absolute;
    top: 306px;
    width: 439px;
    height: 271px;
    border-radius: var(--card-radius);
    box-shadow: 0 2px 6px rgba(0,0,0,0.45);
  }
  .card--front { left: 149px; background: var(--card-white); }
  .card--back  { left: 610px; background: var(--brand-purple); }

  .firm-name {
    position: absolute;
    left: 0;
    right: 0;
    text-align: center;
    font-weight: 600;
    text-transform: uppercase;
    letter-spacing: 1.5px;
    line-height: 1.15;
  }
  .card--front .firm-name { top: 358px; top: 52px; color: var(--brand-purple); font-size: 25px; }
  .card--back .firm-name  { top: 108px; color: var(--card-white); font-size: 27px; }

  .identity {
    position: absolute;
    right: 235px;
    top: 148px;
    text-align: right;
    color: var(--ink);
    font-size: 12.5px;
    line-height: 15px;
  }
  .identity .person {
    color: var(--brand-purple);
    font-weight: 600;
    font-size: 15px;
    line-height: 17px;
  }
  .identity .role { margin-bottom: 13px; }

  .contact {
    position: absolute;
    left: 224px;
    top: 150px;
    color: var(--ink);
    font-size: 12.5px;
    line-height: 15.5px;
    list-style: none;
    margin: 0;
    padding: 0;
  }
  .contact .direct { margin-bottom: 11px; }
  .contact .label { color: var(--brand-purple); font-weight: 600; }
  .contact li { display: flex; align-items: center; gap: 6px; }
  .contact svg { width: 9px; height: 9px; flex: none; fill: var(--brand-purple); }
</style>
</head>
<body>

<section class="card card--front" aria-label="Business card front">
  <div class="firm-name">Law Office of<br>Denise R. Harlow</div>

  <div class="identity">
    <div class="person">Denise R. Harlow, Esq.</div>
    <div class="role">Owner &amp; Founder</div>
    <div>528 E. 19th Street 7th Floor</div>
    <div>New York, NY 10583</div>
  </div>

  <ul class="contact">
    <li class="direct"><span class="label">Direct:</span> (917) 463-5071</li>
    <li>
      <svg viewBox="0 0 10 10" aria-hidden="true"><path d="M2.2 0.5 L3.8 2.6 L2.9 3.6 Q3.9 5.8 6.3 7.1 L7.3 6.1 L9.5 7.7 L8.3 9.5 Q1.2 8 0.5 1.7 Z"/></svg>
      (855) 602-7318
    </li>
    <li>
      <svg viewBox="0 0 10 10" aria-hidden="true"><path d="M0.5 2 H9.5 V8 H0.5 Z M1 2.4 L5 5.4 L9 2.4" stroke="#fff" stroke-width="0.8"/></svg>
      denise@deniserharlowlegal.test
    </li>
    <li>
      <svg viewBox="0 0 10 10" aria-hidden="true"><circle cx="5" cy="5" r="4.5"/><path d="M2 3.5 Q4 4 3.5 6 L5 8 M6 1.5 Q7 3.5 8.5 4" stroke="#fff" stroke-width="0.8" fill="none"/></svg>
      www.deniserharlowlegal.test
    </li>
  </ul>
</section>

<section class="card card--back" aria-label="Business card back">
  <div class="firm-name">Law Office of<br>Denise R. Harlow</div>
</section>

</body>
</html>
```